Modern Podcast Marketing Cards - BRAVOKESTRAL

Update: Do "not" include my address, there's no need for this. Please remember this project needs to promote my brand along with the my new Podcast shows tagline. So this is not a traditional business card, it has to look cool enough so people want to hold onto it and not just toss it aside. So obviously "not" an old school boring business card with a ton of business contact info/text. Needs to catch attention and drive my recipients to want to visit the website " bravokestral.net " and/or to download and listen on the apps Tunevale, Weavly, Mondro Spin. Plus would like to drive them to Follow on my social media channels @BRAVOKESTRAL; all while making sure the the design doesn't look cluttered while not being boring.
I've re-designed the logo specifically for the new show though vs what you see when you first visit my website. So the shows logo is also attached which is found on Tunevale, Weavly app, etc. That design is to promote the three domains this brand focused on "Fueling" the followers and listeners with, regarding "Health", "Business", and "Lifestyle". If logos end up on both sides of the card, one should have the version with the three words included of Health, Business, and Lifestyle. The other side should use the blank version of the logo attached which does not have those three words under the BRAVOKESTRAL logo. So I gave you two versions to work with.
**Try and work in my three domains mentioned above and/or the actual tagline for the show/my brand which is "SPARK Your Health, Business, and Lifestyle". You can break it up a little if it will stand out stronger. Remember this is more of a marketing/advertising card vs a boring traditional business card.
Just to note, my profession behind the Podcast Host is my consulting as a Sales, Marketing, and Business Development consultant, But the final design should really show off my Tagline and those three domains to "SPARK Your Health, Business, and Lifestyle!" (without being cluttered)
- again I like it when the flames get ghosted or used as a transparent backdrop. Or you can somehow take a podcast microphone and overlay my logo's flames to wrap around the microphone or have the microphone stand out with "fire fueling it".
Why the three domains focus?
1. Health: because I'm a health nut, adrenaline junkie sports participant, GritLoop coach, and I have a part time nutritional business.
2. Business: because I'm a business consultant specializing in online branding and social media marketing, with 20 years of business experience.
3. Lifestyle: because I do a lot of coaching on life balance, motivational speaking, love to travel, and am always promoting people to balance their lifestyle between business, personal, and fun.

Target Market(s)

Podcasting, Online Branding & Marketing

Industry/Entity Type

Marketing

Contact Information for Business Card

More of a marketing card than a traditional business card, Double-sided, rich bold colors used from my logo's colors. Will consider the clear plastic style too.

Font styles to use
Serif
Sans Serif

Requirements
Must have
• - Drive people to want to visit the website and download/listen to my podcast via the three apps.
• - So use those apps logos somehow from Tunevale Podcast app, Weavly Radio app, and the Mondro Spin app logos.
• - For contact info: My Name, Titles are Chief Intrepid Officer, also include Podcaster for the 2nd title. Contact info should be 1st my email, 2nd my website address without the www; and third my phone.
• Note: reduce clutter and make sure it's not too busy. That's why I'm considering a 2 sided design.
Nice to have
• - Colors should coincide with my logo and primary colors from the logos.
• - Not too much white, at least side should be a gray or blue backdrop
• - I love the style where you take the flames from my logo and ghost or make them transparent on the backdrop for the background on the card.
• - A podcast microphone logo included somehow or set it one fire with my fire from my logo would be cool.
Should not have
• - Do not list my address
• - No single sided cards
• - No crazy stripes or swoosh marks, emphasis is the FIRE so motivate people, and inspire, "to fire them up" with your design.

```html
<!DOCTYPE html>
<html lang="en">
<head>
<meta charset="utf-8">
<title>SPARK Your Health, Business, and Lifestyle – BRAVOKESTRAL</title>
<link rel="stylesheet" href="https://fonts.googleapis.com/css2?family=Fira+Sans:ital,wght@0,400;0,600;1,700&display=swap">
<style>
  :root {
    --brand-blue: #33509c;
    --ink: #0b0b0b;
    --paper: #ffffff;
    --bar-gray: #d4dddc;
  }
  * { margin: 0; padding: 0; box-sizing: border-box; }
  html, body { width: 725px; height: 1200px; overflow: hidden; background: var(--paper); }
  .card {
    position: relative;
    width: 725px;
    height: 1200px;
    overflow: hidden;
    background: var(--paper);
    font-family: "Fira Sans", Arial, sans-serif;
  }
  .frames, .mic-graphic { position: absolute; left: 0; top: 0; }
  .tagline {
    position: absolute;
    left: 0; top: 0;
    width: 725px;
    font-style: italic;
    font-weight: 700;
    font-size: 42px;
    letter-spacing: -0.5px;
    color: var(--ink);
  }
  .tagline-word { position: absolute; white-space: nowrap; line-height: 1; }
  .spark-box {
    position: absolute;
    left: 115px; top: 117px;
    width: 145px; height: 65px;
    background: var(--ink);
  }
  .spark-word { left: 124px; top: 136px; color: var(--paper); }
  .your-word { left: 266px; top: 136px; }
  .health-word { left: 384px; top: 136px; }
  .business-word { left: 131px; top: 215px; }
  .and-word { left: 131px; top: 294px; }
  .lifestyle-word { left: 131px; top: 373px; }
  .domain { color: var(--brand-blue); }
  .follow-bar {
    position: absolute;
    left: 140px; top: 1044px;
    width: 550px; height: 103px;
    border: 8px solid var(--brand-blue);
    background: var(--bar-gray);
    display: flex;
    align-items: center;
    justify-content: space-between;
    padding: 0 16px 0 18px;
  }
  .network {
    font-family: "Fira Sans", Arial, sans-serif;
    font-weight: 600;
    font-size: 13px;
    color: var(--ink);
  }
  .follow-label {
    font-family: "Fira Sans", Arial, sans-serif;
    font-weight: 400;
    font-size: 20px;
    color: var(--ink);
  }
</style>
</head>
<body>
<main class="card">
  <svg class="frames" width="725" height="1200" viewBox="0 0 725 1200" aria-hidden="true">
    <g fill="none" stroke="var(--brand-blue)" stroke-width="8">
      <polyline points="372,191 372,99 740,99"/>
      <polyline points="372,191 740,191"/>
      <polyline points="-10,191 368,191 368,286 -10,286"/>
      <polyline points="-10,342 503,342 503,433 -10,433"/>
    </g>
  </svg>

  <div class="tagline">
    <div class="spark-box"></div>
    <span class="tagline-word spark-word">SPARK</span>
    <span class="tagline-word your-word">Your</span>
    <span class="tagline-word health-word"><span class="domain">Health</span>,</span>
    <span class="tagline-word business-word"><span class="domain">Business</span>,</span>
    <span class="tagline-word and-word">and</span>
    <span class="tagline-word lifestyle-word"><span class="domain">Lifestyle</span>!</span>
  </div>

  <svg class="mic-graphic" width="725" height="1200" viewBox="0 0 725 1200" role="img" aria-label="Podcast microphone broadcasting">
    <g fill="none" stroke="var(--ink)" stroke-width="10" stroke-linecap="round">
      <path d="M291,590 A75,75 0 0 1 411,590"/>
      <path d="M315,610 A45,45 0 0 1 387,610"/>
      <path d="M306,690 L306,710 A45,45 0 0 0 396,710 L396,690"/>
      <line x1="351" y1="755" x2="351" y2="785"/>
    </g>
    <rect x="326" y="633" width="50" height="105" rx="25" fill="var(--ink)"/>
    <rect x="330" y="781" width="42" height="12" fill="var(--ink)"/>
    <rect x="330" y="801" width="44" height="248" fill="var(--brand-blue)"/>
  </svg>

  <nav class="follow-bar" aria-label="Social channels">
    <span class="network">Facio</span>
    <span class="network">Chirpa</span>
    <span class="network">Gplex</span>
    <span class="network">Linko</span>
    <span class="network">Pinvo</span>
    <span class="network">Tumbo</span>
    <span class="network">Vidro</span>
    <span class="network">Snapli</span>
    <span class="network">Feed</span>
    <span class="follow-label">Follow us</span>
  </nav>
</main>
</body>
</html>
```